Stellenanzeige für einen Auszubildenden
Zielgruppe
Wir sind ein Unternehmen im Bereich Spritzgusstechnik und verfügen über einen eigenen Werkzeugbau mit Konstruktion und eine additive Fertigung. Wir fertigen technische Kunststoffteile und Baugruppen für die Nutzfahrzeug-, Elektronik-, Elektrotechnik- und Hausgeräteindustrie. Unser Produktspektrum ist vielfältig und abwechslungsreich und hält ständig interessante Herausforderungen bereit.
Aufgabenstellung
Wir benötigen eine Stellenanzeige für einen Auszubildenden im Berufsbild 'Kunststofftechnologe (m/w/d)'. Die Anzeige wird auf einem Werbeflyer abgedruckt, der an Haushalte verteilt wird. Der Flyer bewirbt eine Aktion eines regionalen Vereins. Wir sponsern diesen Flyer mit unsere Anzeige. Der Flyer wird in der Größe DIN A 5 beidseitig bedruckt gefertigt, unsere Anzeige darf die Fläche DIN A 6 (Querformat) einnehmen. Der Flyer wird farbig gedruckt.
Infos zur Ausbildungsstelle sind auf https://www.brantova.de/azubi.html zu finden. Diese müssen jedoch nicht alle auf der Anzeige erscheinen. Vielmehr soll die Anzeige Interesse wecken. Die Interessenten sollen dann alle detaillierten Informationen zur Ausbildung über den Link auf unserer Web-Seite abrufen.
Wichtig ist evtl. folgender Bonus:
'Bei guten Leistungen erhältst Du ab dem zweiten Ausbildungsjahr einen 3D-Drucker und ein professionelles 3D-CAD-Programm für die Nutzung zu Hause zur Verfügung gestellt.' Eventuell kann diese Info - gerne verkürzt - in die Anzeige integriert werden.
Unser Firmenlogo füge ich als Datei an.

```html
<!DOCTYPE html>
<html lang="de">
<head>
<meta charset="utf-8">
<title>Brantova – Ausbildung Kunststofftechnologe</title>
<link rel="stylesheet" href="https://fonts.googleapis.com/css2?family=Anton&family=Barlow:wght@400;500;600;700&family=Montserrat:ital,wght@0,600;1,700&display=swap">
<style>
:root{
  --green:#3fae49;
  --green-dark:#2f8f39;
  --ink:#1d1d1b;
  --white:#ffffff;
  --bg:#d9d9d9;
  --photo-a:#2c4f7c;
  --photo-b:#9fb4cc;
}
*{margin:0;padding:0;box-sizing:border-box}
html,body{width:842px;height:1200px;overflow:hidden;background:var(--bg)}
.canvas{position:relative;width:842px;height:1200px}
.ad{position:absolute;left:21px;top:317px;width:800px;height:566px;background:var(--white);overflow:hidden;box-shadow:0 4px 14px rgba(0,0,0,.25);font-family:"Barlow",sans-serif;color:var(--ink)}
.ad__half{position:absolute;top:0;width:400px;height:566px;overflow:hidden}
.ad__half--intro{left:0}
.ad__half--offer{left:400px}
.ad svg.shapes{position:absolute;inset:0}
.abs{position:absolute}

.brand{font-family:"Barlow",sans-serif;font-weight:700;color:var(--green);letter-spacing:.5px;display:flex;align-items:center;gap:6px}
.brand__mark{width:10px;height:10px;background:var(--green)}
.brand--main{left:30px;top:24px;font-size:24px}
.brand--small{left:236px;top:220px;font-size:18px}

.bubble__lead{left:40px;width:330px;top:270px;text-align:center;font-family:"Montserrat",sans-serif;font-style:italic;font-weight:700;font-size:10.5px;color:var(--white)}
.bubble__title{left:36px;width:336px;top:285px;text-align:center;font-family:"Anton",sans-serif;font-weight:400;font-size:25px;line-height:1.15;color:var(--white)}
.bubble__sub{left:40px;width:330px;top:325px;text-align:center;font-family:"Montserrat",sans-serif;font-weight:600;font-size:11.5px;line-height:1.25;color:var(--white)}

.tasks{left:38px;top:426px;width:250px}
.tasks__title{font-weight:600;font-size:16px;color:var(--green);margin-bottom:3px}
.tasks__text{font-size:7.6px;line-height:1.32}

.offer__title{left:58px;top:28px;padding:0 8px;background:var(--white);font-family:"Anton",sans-serif;font-weight:400;font-size:17px;color:var(--green)}
.offer__list{left:52px;top:62px;width:300px;list-style:none}
.offer__list li{position:relative;padding-left:12px;font-size:8.2px;line-height:1.25;margin-bottom:9px}
.offer__list li svg{position:absolute;left:0;top:1px;width:7px;height:7px}

.contact{left:40px;top:318px;width:330px;color:var(--white)}
.contact__title{font-family:"Anton",sans-serif;font-weight:400;font-size:17px;margin-bottom:4px}
.contact p{font-size:7.8px;line-height:1.35;margin-bottom:6px}
.contact strong{font-weight:700}
.contact__link{font-size:8.6px !important}
.bonus{left:30px;top:502px;width:340px;text-align:center;font-weight:700;font-size:8.6px;line-height:1.35}
</style>
</head>
<body>
<main class="canvas">

  <section class="ad">

    <div class="ad__half ad__half--intro">
      <svg class="shapes" width="400" height="566" viewBox="0 0 400 566">
        <defs>
          <linearGradient id="photoTone" x1="0" y1="0" x2="1" y2="1">
            <stop offset="0" stop-color="var(--photo-b)"/>
            <stop offset="1" stop-color="var(--photo-a)"/>
          </linearGradient>
        </defs>
        <path role="img" aria-label="Foto: junge Auszubildende mit Schutzhelm und Schutzbrille vor einer Spritzgussmaschine" d="M0 70 L170 70 Q200 70 212 40 L232 0 L400 0 L400 245 L0 350 Z" fill="url(#photoTone)"/>
        <path d="M34 268 Q30 256 44 254 L366 240 Q380 240 378 254 L372 378 Q370 392 356 392 L118 400 L84 428 L86 402 L48 404 Q36 404 36 392 Z" fill="var(--green-dark)"/>
        <path d="M30 262 Q28 250 42 248 L362 234 Q376 234 374 248 L368 372 Q366 386 352 386 L114 394 L82 420 L84 396 L46 398 Q34 398 34 386 Z" fill="var(--green)"/>
        <path d="M0 566 L0 552 Q10 538 40 536 L400 530 L400 566 Z" fill="var(--green)"/>
      </svg>

      <div class="abs brand brand--main"><span class="brand__mark"></span>BRANTOVA</div>

      <p class="abs bubble__lead">Wir bieten eine Ausbildungsstelle zum</p>
      <h1 class="abs bubble__title">Kunststofftechnologe (m/w/d)</h1>
      <p class="abs bubble__sub">Fachrichtung Formteile auf<br>Wunsch mit der Zusatzqualifikation<br>additive Fertigung</p>

      <div class="abs tasks">
        <h2 class="tasks__title">Deine Aufgaben sind</h2>
        <p class="tasks__text">die Vorbereitung und die genaue Einstellung der Maschinen und Anlagen für die Fertigung unserer Kunststoffteile. Du kontrollierst und überwachst den Fertigungsablauf, überprüfst regelmäßig die Qualität der Produkte und greifst notfalls korrigierend ein. Des Weiteren bist Du als Kunststofftechnologe für die Anleitung von Personal in der Fertigung und die Wartung und Instandhaltung der Maschinen sowie der Werkzeuge und Formen zuständig.</p>
      </div>
    </div>

    <div class="ad__half ad__half--offer">
      <svg class="shapes" width="400" height="566" viewBox="0 0 400 566">
        <path d="M0 318 L400 290 L400 470 L0 494 Z" fill="var(--green)"/>
        <rect x="36" y="42" width="330" height="240" fill="var(--white)" stroke="var(--green)" stroke-width="2"/>
        <path d="M400 566 L400 552 Q392 546 372 546 L270 548 Q248 550 240 566 Z" fill="var(--green)"/>
      </svg>

      <h2 class="abs offer__title">Wir bieten Dir</h2>
      <ul class="abs offer__list">
        <li><svg viewBox="0 0 10 10"><path d="M1 5 L4 8 L9 2" fill="none" stroke="var(--green)" stroke-width="2"/></svg>eine Ausbildungsvergütung entsprechen der Leistungen im Metallhandwerk.</li>
        <li><svg viewBox="0 0 10 10"><path d="M1 5 L4 8 L9 2" fill="none" stroke="var(--green)" stroke-width="2"/></svg>Übernahme bei guter Leistung im Betrieb und in der Berufsschule.</li>
        <li><svg viewBox="0 0 10 10"><path d="M1 5 L4 8 L9 2" fill="none" stroke="var(--green)" stroke-width="2"/></svg>Wenn Du Dich für die Zusatzqualifikation additive Fertigung entscheidest, lernst Du die 3D-Konstruktion mit modernen CAD Systemen kennen und arbeitest mit verschiedenen 3D-Druckern.</li>
        <li><svg viewBox="0 0 10 10"><path d="M1 5 L4 8 L9 2" fill="none" stroke="var(--green)" stroke-width="2"/></svg>Bei guten Leistungen erhältst Du ab dem zweiten Ausbildungsjahr einen 3D-Drucker und ein professionelles 3D-CAD-Programm für die Nutzung zu Hause zur Verfügung gestellt.</li>
        <li><svg viewBox="0 0 10 10"><path d="M1 5 L4 8 L9 2" fill="none" stroke="var(--green)" stroke-width="2"/></svg>Flache Hierarchien und Flexibilität</li>
        <li><svg viewBox="0 0 10 10"><path d="M1 5 L4 8 L9 2" fill="none" stroke="var(--green)" stroke-width="2"/></svg>kostenfreie Arbeitskleidung</li>
        <li><svg viewBox="0 0 10 10"><path d="M1 5 L4 8 L9 2" fill="none" stroke="var(--green)" stroke-width="2"/></svg>kostenfreie Getränke</li>
        <li><svg viewBox="0 0 10 10"><path d="M1 5 L4 8 L9 2" fill="none" stroke="var(--green)" stroke-width="2"/></svg>kostenfreies Bio-Obst</li>
        <li><svg viewBox="0 0 10 10"><path d="M1 5 L4 8 L9 2" fill="none" stroke="var(--green)" stroke-width="2"/></svg>4 ½-Tage Woche ohne Schicht- und Wochenendarbeit</li>
      </ul>

      <div class="abs brand brand--small"><span class="brand__mark"></span>BRANTOVA</div>

      <div class="abs contact">
        <h2 class="contact__title">Interessiert?</h2>
        <p>Die Ausbildung beginnt am 01.09.2024, gerne nehmen wir aber auch Bewerbungen an, die sich nicht mit diesem Datum vereinbaren lassen. Sende uns bitte Deine kompletten Bewerbungsunterlagen (Anschreiben, Lebenslauf, Zeugnisse), unter Angabe des frühestmöglichen Eintrittstermins per E-Mail an <strong>bewerbung@brantova.de.</strong></p>
        <p>Für Rückfragen stehen wir Dir telefonisch unter <strong>07571-5550123</strong> gerne zur Verfügung. Einige weitere Details haben wir für Dich in den FAQ zur Ausbildung zusammengestellt:</p>
        <p class="contact__link"><strong>https://www.brantova.de/azubi.html</strong></p>
      </div>

      <p class="abs bonus">Bei guten Leistungen erhältst Du ab dem zweiten Ausbildungsjahr einen 3D-Drucker und ein professionelles 3D-CAD-Programm für die Nutzung zu Hause zur Verfügung gestellt.</p>
    </div>

  </section>

</main>
</body>
</html>
```